Our new beauty salon requires a price list brochure

Our beauty clinic is a medical grade skin care clinic. So our salon is very clinical and professional in appearance. I would like the colours to be similar to our logo design with some nice texture or abstract shapes thrown in.
Pricelist, contact details and logo is attached
I would prefer it to be a 3 fold brochure.

Target Market(s)

Females aged 30-50

Colors
85acd3
cedeed
c4c4c4
5c5c5c
000000
ffffff
eea3c7
f9d9e8
dbdbdb

Requirements
Must have
• easy to read

```html
<!DOCTYPE html>
<html lang="en">
<head>
<meta charset="utf-8">
<title>Solace Aesthetics – Price List Brochure</title>
<link href="https://fonts.googleapis.com/css2?family=Jost:wght@300;400&family=Josefin+Sans:wght@300;400&display=swap" rel="stylesheet">
<style>
  :root{
    --page:#f4f4f5;
    --navy:#2e4560;
    --slate:#7f8b98;
    --mist:#e3e4e7;
    --row:#c9ccd2;
    --ink:#1f2a36;
    --white:#ffffff;
    --brand:#3b5068;
  }
  *{box-sizing:border-box;margin:0;padding:0}
  html,body{width:1200px;height:1200px;overflow:hidden;background:var(--page)}
  body{font-family:"Jost",sans-serif;color:var(--ink)}
  .brochure{position:absolute;left:60px;top:185px;width:1080px;height:830px;display:flex;box-shadow:0 18px 40px rgba(0,0,0,.12)}
  .panel{position:relative;width:360px;height:830px;overflow:hidden}
  .panel-bg{position:absolute;inset:0;width:100%;height:100%}

  /* price list */
  .prices{background:var(--mist)}
  .price-list{position:absolute;left:18px;right:18px;top:26px;display:flex;flex-direction:column}
  .section-title{background:var(--navy);color:var(--white);font-family:"Josefin Sans",sans-serif;font-weight:300;font-size:12.5px;letter-spacing:.12em;text-align:center;padding:15px 8px 8px;line-height:1.35;text-transform:uppercase}
  .group{margin-top:12px}
  .group-title{background:var(--row);font-size:13px;text-align:center;padding:5px 0 3px}
  .group-title em{font-style:italic;font-size:12px}
  .row{display:flex;align-items:stretch;background:var(--row);border-top:1px solid rgba(255,255,255,.55)}
  .row-name{flex:1;font-size:13px;padding:6px 6px 3px;line-height:1.3}
  .row-price{width:48px;flex:none;background:var(--navy);color:var(--white);font-size:13px;text-align:right;padding:5px 6px 3px;border-top:1px solid rgba(255,255,255,.6)}
  .section{margin-top:16px}
  .section:first-child{margin-top:0}
  .section .row:first-of-type{margin-top:12px}

  /* middle */
  .contact-block{position:absolute;left:0;right:0;bottom:34px;text-align:center}
  .brand-name{font-family:"Jost",sans-serif;font-weight:300;color:var(--brand);font-size:58px;letter-spacing:.02em;line-height:1}
  .brand-sub{font-family:"Josefin Sans",sans-serif;font-weight:300;color:var(--brand);font-size:12px;letter-spacing:.7em;margin-top:8px;padding-left:.7em}
  .address{font-family:"Josefin Sans",sans-serif;font-weight:300;font-style:normal;color:var(--slate);font-size:15px;letter-spacing:.1em;line-height:1.35;margin-top:6px}

  /* cover */
  .cover-image{position:absolute;inset:0;background:linear-gradient(180deg,#c9cbcf 0%,#e6e6e7 22%,#d8d5d4 42%,#8c8d93 62%,#a08d8c 78%,#5a6170 100%)}
  .cover-logo{position:absolute;top:100px;left:0;right:0;text-align:center}
  .cover-details{position:absolute;left:0;right:0;bottom:40px;text-align:center;color:var(--white)}
  .web{font-family:"Josefin Sans",sans-serif;font-weight:300;font-size:17px;letter-spacing:.14em}
  .social{font-size:13px;font-weight:300;margin-top:6px;display:flex;align-items:center;justify-content:center;gap:6px}
  .social-dot{width:10px;height:10px;border-radius:50%;background:var(--white)}
  .social + .social{margin-top:3px}
</style>
</head>
<body>
<main class="brochure">

  <section class="panel prices">
    <svg class="panel-bg" viewBox="0 0 360 830" preserveAspectRatio="none" aria-hidden="true">
      <polygon points="0,0 360,0 360,450 0,370" fill="#8a96a3"/>
    </svg>
    <div class="price-list">
      <div class="section">
        <h2 class="section-title">Chemical Peels</h2>
        <div class="group">
          <div class="group-title">Verity Dr Peels <em>30min</em></div>
          <div class="row"><span class="row-name">Lactic Acid Peels 20% - 40% - 60%</span><span class="row-price">$120</span></div>
          <div class="row"><span class="row-name">Age Renewal Peel</span><span class="row-price">$120</span></div>
          <div class="row"><span class="row-name">Even Tone Pigment Peel</span><span class="row-price">$120</span></div>
          <div class="row"><span class="row-name">Clear Skin Peel</span><span class="row-price">$120</span></div>
        </div>
        <div class="group">
          <div class="group-title">Clarelle Peels <em>30min</em></div>
          <div class="row"><span class="row-name">Berry Glow Peel</span><span class="row-price">$120</span></div>
          <div class="row"><span class="row-name">Fruit Enzyme Peel</span><span class="row-price">$120</span></div>
          <div class="row"><span class="row-name">Balance Peel</span><span class="row-price">$120</span></div>
          <div class="row"><span class="row-name">Pure Retinol Peel</span><span class="row-price">$250</span></div>
        </div>
      </div>
      <div class="section">
        <h2 class="section-title">Lumina LED</h2>
        <div class="row"><span class="row-name">Per Treatment</span><span class="row-price">$90</span></div>
        <div class="row"><span class="row-name">When added on to any of our other skin treatments.</span><span class="row-price">$50</span></div>
      </div>
      <div class="section">
        <h2 class="section-title">Dermaline Microneedling<br>(Collagen Induction Therapy)</h2>
        <div class="row"><span class="row-name">Full Face</span><span class="row-price">$350</span></div>
        <div class="row"><span class="row-name">Face, Neck And Décolletage</span><span class="row-price">$450</span></div>
      </div>
      <div class="section">
        <h2 class="section-title">Novalux Laser Facial</h2>
        <div class="row"><span class="row-name">Full Face</span><span class="row-price">$350</span></div>
        <div class="row"><span class="row-name">Face, Neck And Décolletage</span><span class="row-price">$450</span></div>
      </div>
    </div>
  </section>

  <section class="panel contact">
    <svg class="panel-bg" viewBox="0 0 360 830" preserveAspectRatio="none" aria-hidden="true">
      <defs>
        <linearGradient id="slateFade" x1="0" y1="0" x2="1" y2="0">
          <stop offset="0" stop-color="#8b97a4"/>
          <stop offset=".5" stop-color="#a1abb6"/>
          <stop offset="1" stop-color="#7c8895"/>
        </linearGradient>
      </defs>
      <rect width="360" height="830" fill="#e6e7e9"/>
      <polygon points="0,0 360,0 360,580 0,450" fill="url(#slateFade)"/>
    </svg>
    <div class="contact-block">
      <div class="brand-name">solace</div>
      <div class="brand-sub">AESTHETICS</div>
      <address class="address">
        14/220 Coastal Road<br>Seabrook Bay<br>Western Australia<br>(08) 9000 1234
      </address>
    </div>
  </section>

  <section class="panel cover">
    <div class="cover-image" role="img" aria-label="Soft-focus photograph of a makeup brush and an eyeshadow palette in nude tones"></div>
    <svg class="panel-bg" viewBox="0 0 360 830" preserveAspectRatio="none" aria-hidden="true">
      <path d="M0,330 C120,420 260,520 360,680 L360,830 L0,830 Z" fill="#3f5166" opacity=".55"/>
      <path d="M0,500 C150,520 280,600 360,760 L360,830 L0,830 Z" fill="#3a4a5e" opacity=".35"/>
    </svg>
    <div class="cover-logo">
      <div class="brand-name">solace</div>
      <div class="brand-sub">AESTHETICS</div>
    </div>
    <div class="cover-details">
      <div class="web">www.solaceaesthetics.com.au</div>
      <div class="social"><span class="social-dot"></span>solace_aesthetics</div>
      <div class="social"><span class="social-dot"></span>solace_aesthetics_au</div>
    </div>
  </section>

</main>
</body>
</html>
```